Etiketten-Design für Brause in der Flasche gesucht
Zielgruppe
Wir sind eine kleine Brauerei. Wir haben hier schon unsere Bieretiketten designen lassen.
Aufgabenstellung
Nun suchen wir Etiketten für 0,33l Falschen für unsere Brause...Momentan haben wir z.B. Rharbarber gemacht.
Es werden aber noch noch andere gemacht..also evtl ein Design das man den verschiedenen Früchten anpassen kann.
Unser Logo vom Hof sollte mit eingebaut werden.

```html
<!DOCTYPE html>
<html lang="de">
<head>
<meta charset="utf-8">
<title>Hof Lindert Brause – Etiketten</title>
<link rel="stylesheet" href="https://fonts.googleapis.com/css2?family=Open+Sans:wght@400;600&family=Kaushan+Script&family=Courgette&display=swap">
<style>
  :root {
    --bg: #eef1f2;
    --purple: #9a2a86;
    --purple-dark: #7c1d6c;
    --purple-light: #b8479f;
    --white: #ffffff;
    --label-white: #f1f0f2;
    --ink: #2a2a2a;
  }
  * { margin: 0; padding: 0; box-sizing: border-box; }
  html, body { width: 721px; height: 1200px; overflow: hidden; }
  body { background: var(--bg); position: relative; font-family: "Open Sans", sans-serif; }

  /* Neck label */
  .neck-label {
    position: absolute; left: 213px; top: 60px; width: 295px; height: 255px;
    background: linear-gradient(90deg, var(--purple-dark), var(--purple-light) 50%, var(--purple-dark));
    color: var(--white); text-align: center;
  }
  .neck-label .brand-dot {
    width: 66px; height: 66px; border: 3px solid var(--white); border-radius: 50%;
    margin: 58px auto 10px;
  }
  .neck-label .brand-name { font-weight: 600; font-size: 36px; line-height: 1.1; }
  .neck-label .brand-place { font-size: 17px; letter-spacing: 4px; margin-top: 2px; }

  /* Body label */
  .body-label { position: absolute; left: 70px; top: 380px; width: 580px; height: 735px; overflow: hidden; }
  .band { position: absolute; left: 0; width: 100%; }
  .band-top, .band-bottom {
    background: radial-gradient(ellipse at center, var(--purple-light), var(--purple) 70%, var(--purple-dark));
  }
  .band-top { top: 0; height: 140px; }
  .stripe-white { top: 140px; height: 8px; background: var(--white); }
  .stripe-purple { top: 148px; height: 18px; background: var(--purple); }
  .band-middle { top: 166px; height: 346px; background: linear-gradient(90deg, #dcdadd, var(--label-white) 50%, #dcdadd); }
  .band-bottom { top: 512px; height: 223px; }
  .fine-print {
    position: absolute; left: 0; bottom: 22px; width: 100%;
    color: var(--white); font-size: 17px; white-space: nowrap; overflow: hidden;
  }

  .oval {
    position: absolute; left: 85px; top: 78px; width: 410px; height: 565px;
    border-radius: 50%; background: var(--white); border: 4px solid var(--purple);
    box-shadow: inset 0 0 0 10px var(--white), inset 0 0 0 12px var(--purple);
    text-align: center;
  }
  .oval .brand-dot {
    width: 86px; height: 86px; border: 4px solid var(--ink); border-radius: 50%;
    margin: 52px auto 10px;
  }
  .oval .brand-name { color: var(--ink); font-weight: 600; font-size: 44px; line-height: 1.1; }
  .oval .brand-place { color: var(--ink); font-size: 21px; letter-spacing: 5px; margin-top: 4px; }
  .product-name {
    font-family: "Kaushan Script", cursive; color: var(--ink);
    font-size: 118px; line-height: 1; margin-top: 2px; margin-left: -40px; margin-right: -40px;
  }
  .flavour {
    font-family: "Courgette", cursive; color: var(--purple);
    font-size: 50px; line-height: 1.15; margin-top: 22px;
  }
</style>
</head>
<body>
  <section class="neck-label">
    <div class="brand-dot"></div>
    <div class="brand-name">Hof Lindert</div>
    <div class="brand-place">FALKENRIED</div>
  </section>

  <section class="body-label">
    <div class="band band-top" role="img" aria-label="Lila Band mit Kreismuster"></div>
    <div class="band stripe-white"></div>
    <div class="band stripe-purple"></div>
    <div class="band band-middle"></div>
    <div class="band band-bottom" role="img" aria-label="Lila Band mit Kreismuster"></div>
    <p class="fine-print">Lorem ipsum dolor sit amet, consectetuer adipiscing elit, s</p>

    <div class="oval">
      <div class="brand-dot"></div>
      <div class="brand-name">Hof Lindert</div>
      <div class="brand-place">FALKENRIED</div>
      <div class="product-name">Brause</div>
      <div class="flavour">Rharbarber<br>Flavour</div>
    </div>
  </section>
</body>
</html>
```